Brightkoru NZ Brand, Revenue, Promotions & Events

I need an innovative business card that pops my brand. I like the colours against darker gradients and i'm not afraid to be bold.

I run my own Business, Brand, Event & Promotion company. I specialise in breathing life into businesses and adding atmosphere to promotions and events. I am concept based lady that likes to test the boundaries and create stand out campaigns that connect with the consumer.

I have 12 years business experience in a realm of interesting fields form 11 years in coordinating international music festivals & promotions, 6 years in radio with 8 radio awards including a NZ radio award for best sales team in NZ and was the national brand and sales manager for New Zealands 1st indoor entertainment mall. With 10 years of experience in advertising sales, I have an eye for creating revenue streams for businesses and thrive on implementing campaigns that compliment those streams.

I love sayings like "Do what you love, love what you do" and believe that you can achieve anything you want.

I have been fortunate in my career that my connections have carried me without needing to promote my business however it is important that I start to do so.

Target Market(s)

Decision makers 25 to 54

Contact Information for Business Card

Petra Holsworth
Director
p. 022 739 5081
e. petra@brightkoru.example
www.brightkoru.example

FB, IG and Linkedin logo

Font styles to use
Sans Serif

Colors

Designer to choose colors to be used in the design.

Requirements
Must have
• Petra Holsworth
• Director
• p. 022 739 5081
• e. petra@brightkoru.example
• www.brightkoru.example
• FB, IG and Linkedin logo
Nice to have
• I am looking for a business card with character, that leaves my presence with my customer and makes them remember my brand & optimistic personality when i walk out the door.

```html
<!DOCTYPE html>
<html lang="en">
<head>
<meta charset="utf-8">
<title>Brightkoru NZ – Business Card</title>
<link rel="stylesheet" href="https://fonts.googleapis.com/css2?family=Open+Sans:ital,wght@0,400;0,600;0,700;1,700&family=Montserrat:wght@600&display=swap">
<style>
  :root {
    --backdrop: #2a2b2d;
    --brand-blue: #29a9e1;
    --card-white: #ffffff;
    --ink-dark: #2b2b2b;
    --ink-grey: #9a9a9a;
    --radius: 26px;
  }
  * { box-sizing: border-box; margin: 0; padding: 0; }
  html, body {
    width: 1200px; height: 900px; overflow: hidden;
    background: var(--backdrop);
    font-family: "Open Sans", Arial, sans-serif;
  }
  .canvas {
    width: 1200px; height: 900px;
    display: flex; flex-direction: column; align-items: center; justify-content: center;
    gap: 36px;
  }
  .card {
    position: relative;
    width: 700px; height: 400px;
    border-radius: var(--radius);
    overflow: hidden;
    box-shadow: 0 14px 30px rgba(0,0,0,.45);
  }
  /* Front */
  .card--front {
    background: var(--brand-blue);
    display: flex; flex-direction: column; align-items: center; justify-content: center;
    color: var(--card-white);
  }
  .wordmark {
    font-family: "Montserrat", "Open Sans", sans-serif;
    font-weight: 600;
    letter-spacing: 3px;
    text-transform: uppercase;
    line-height: 1;
  }
  .card--front .wordmark { font-size: 58px; color: var(--card-white); }
  .tagline {
    font-family: "Open Sans", Arial, sans-serif;
    font-weight: 400;
    text-transform: uppercase;
    letter-spacing: 1px;
  }
  .card--front .tagline { font-size: 17.5px; margin-top: 10px; color: var(--card-white); }

  /* Back */
  .card--back { background: var(--card-white); }
  .person { position: absolute; left: 52px; top: 46px; }
  .person__name {
    font-weight: 700; font-style: italic; font-size: 32px;
    color: var(--brand-blue); letter-spacing: .2px;
  }
  .person__role { font-size: 16px; color: var(--ink-dark); margin-top: 0; }
  .back-brand {
    position: absolute; right: 46px; top: 150px; text-align: right;
  }
  .card--back .wordmark { font-size: 40px; color: var(--brand-blue); }
  .card--back .tagline { font-size: 12px; color: var(--ink-grey); margin-top: 8px; }
  .contact-band {
    position: absolute; left: 0; bottom: 0;
    width: 600px; height: 172px;
    background: var(--brand-blue);
    border-top-right-radius: 86px 172px;
  }
  .contact-list {
    list-style: none;
    position: absolute; left: 40px; top: 36px;
    color: var(--card-white);
    font-size: 19px; line-height: 1.5;
  }
  .contact-list li { display: flex; align-items: center; gap: 12px; }
  .contact-icon { width: 17px; height: 17px; flex: none; }
</style>
</head>
<body>
<main class="canvas">
  <section class="card card--front" aria-label="Business card front">
    <div class="wordmark">Brightkoru NZ</div>
    <div class="tagline">Brand | Revenue | Events &amp; Promotions</div>
  </section>

  <section class="card card--back" aria-label="Business card back">
    <div class="person">
      <div class="person__name">Petra Holsworth</div>
      <div class="person__role">Director</div>
    </div>

    <div class="back-brand">
      <div class="wordmark">Brightkoru NZ</div>
      <div class="tagline">Brand | Revenue | Events &amp; Promotions</div>
    </div>

    <div class="contact-band">
      <ul class="contact-list">
        <li>
          <svg class="contact-icon" viewBox="0 0 20 20" aria-hidden="true">
            <circle cx="10" cy="10" r="10" fill="#fff"/>
            <path d="M7 5.5l1.6 2.4-1 1.1c.6 1.3 1.5 2.2 2.8 2.8l1.1-1 2.4 1.6-.8 1.8c-3.6-.2-6.7-3.3-6.9-6.9z" fill="var(--brand-blue)"/>
          </svg>
          022 739 5081
        </li>
        <li>
          <svg class="contact-icon" viewBox="0 0 20 20" aria-hidden="true">
            <circle cx="10" cy="10" r="10" fill="#fff"/>
            <rect x="5" y="6.5" width="10" height="7" rx="1" fill="var(--brand-blue)"/>
            <path d="M5.5 7l4.5 3.5L14.5 7" stroke="#fff" stroke-width="1" fill="none"/>
          </svg>
          petra@brightkoru.example
        </li>
        <li>
          <svg class="contact-icon" viewBox="0 0 20 20" aria-hidden="true">
            <circle cx="10" cy="10" r="10" fill="#fff"/>
            <circle cx="10" cy="10" r="5" fill="none" stroke="var(--brand-blue)" stroke-width="1.3"/>
            <ellipse cx="10" cy="10" rx="2.2" ry="5" fill="none" stroke="var(--brand-blue)" stroke-width="1.1"/>
            <path d="M5 10h10" stroke="var(--brand-blue)" stroke-width="1.1"/>
          </svg>
          www.brightkoru.example
        </li>
      </ul>
    </div>
  </section>
</main>
</body>
</html>
```